Start up needs juice bottle label design

Tarbeck Sunvale juice company needs juice bottle label design for all natural lemonades, teas, smoothies and cold-pressed juice. We would like the design to have a space for multiple flavors or custom recipes for special orders. Below is the company logo.

Target Market(s)

On-the-go Health conscious

```html
<!DOCTYPE html>
<html lang="en">
<head>
<meta charset="utf-8">
<title>Tarbeck Sunvale – Cold Pressed Juice Label</title>
<link href="https://fonts.googleapis.com/css2?family=Amatic+SC:wght@400;700&family=Roboto:wght@900&family=Kalam:wght@700&display=swap" rel="stylesheet">
<style>
  :root {
    --backdrop: #e6e6e6;
    --label-maroon: #5a0c26;
    --ink-black: #0b0b0b;
    --paper-white: #ffffff;
    --brand-cyan: #3ec3f0;
  }
  html, body {
    margin: 0;
    padding: 0;
    width: 1200px;
    height: 1200px;
    overflow: hidden;
    background: var(--backdrop);
  }
  .label {
    position: absolute;
    left: 397px;
    top: 120px;
    width: 405px;
    height: 959px;
    background: var(--label-maroon);
    color: var(--paper-white);
    font-family: "Amatic SC", cursive;
  }
  .brand-name {
    position: absolute;
    left: 0;
    right: 0;
    top: 62px;
    text-align: center;
    font-family: "Amatic SC", cursive;
    font-weight: 700;
    font-size: 74px;
    line-height: 1;
    color: var(--brand-cyan);
  }
  .tag {
    position: absolute;
    background: var(--ink-black);
    text-align: center;
    font-weight: 700;
    line-height: 1;
  }
  .tag--cold {
    left: 43px;
    top: 200px;
    width: 323px;
    height: 91px;
    font-size: 80px;
    padding-top: 4px;
    box-sizing: border-box;
  }
  .tag--juice {
    left: 130px;
    top: 291px;
    width: 155px;
    height: 83px;
    font-size: 80px;
    transform: rotate(-1.5deg);
  }
  .graphic-slot {
    position: absolute;
    left: 0;
    right: 0;
    top: 404px;
    text-align: center;
    font-family: "Roboto", sans-serif;
    font-weight: 900;
    font-size: 60px;
    line-height: 81px;
    letter-spacing: 1px;
  }
  .flavor-name {
    position: absolute;
    left: 0;
    right: 0;
    top: 660px;
    text-align: center;
    font-size: 54px;
    font-weight: 400;
    line-height: 1;
  }
  .flavor-note {
    position: absolute;
    left: 0;
    right: 0;
    top: 722px;
    text-align: center;
    font-size: 30px;
    font-weight: 400;
    line-height: 1;
  }
  .claims {
    position: absolute;
    left: 0;
    right: 0;
    top: 771px;
    height: 74px;
  }
  .claim {
    position: absolute;
    top: 14px;
    font-size: 46px;
    line-height: 1;
  }
  .claim--fresh { left: 60px; }
  .claim--natural { left: 236px; }
  .leaf-badge {
    position: absolute;
    left: 147px;
    top: 0;
    width: 74px;
    height: 74px;
  }
  .volume {
    position: absolute;
    left: 146px;
    top: 864px;
    width: 115px;
    height: 53px;
    background: var(--ink-black);
    border-radius: 4px;
    text-align: center;
    font-family: "Kalam", cursive;
    font-weight: 700;
    font-size: 30px;
    line-height: 56px;
  }
</style>
</head>
<body>
  <main class="label">
    <div class="brand-name">Tarbeck Sunvale</div>

    <div class="tag tag--cold">COLD PRESSED</div>
    <div class="tag tag--juice">JUICE</div>

    <div class="graphic-slot">ADD<br>GRAPHIC<br>HERE</div>

    <div class="flavor-name">FLAVOR</div>
    <div class="flavor-note">NO SUGAR ADDED</div>

    <div class="claims">
      <span class="claim claim--fresh">FRESH</span>
      <svg class="leaf-badge" viewBox="0 0 74 74" aria-hidden="true">
        <circle cx="37" cy="37" r="33" fill="none" stroke="#ffffff" stroke-width="3"/>
        <path d="M35 52 C22 48 18 36 22 24 C32 28 38 38 35 52 Z" fill="#ffffff"/>
        <path d="M39 52 C52 48 56 36 52 24 C42 28 36 38 39 52 Z" fill="#ffffff"/>
      </svg>
      <span class="claim claim--natural">NATURAL</span>
    </div>

    <div class="volume">473mL</div>
  </main>
</body>
</html>
```